New Flyer Design Project Brenwick Doors and Interiors

Real photos will be added but please start with these for layout. Copy will be supplied so you can just leave a text box to start I am open to suggestions. Thank you

Target Market(s)

Builders, Designers, remodelers, consumers

Colors

Designer to choose colors to be used in the design.

Requirements
Must have
• Before and after photos, email, phone, logo, description

```html
<!DOCTYPE html>
<html lang="en">
<head>
<meta charset="utf-8">
<title>Brenwick Doors and Interiors – Flyer</title>
<link rel="stylesheet" href="https://fonts.googleapis.com/css2?family=Lato:wght@400;700;900&display=swap">
<style>
  :root {
    --stage: #16181c;
    --wood-dark: #2a1a10;
    --wood-mid: #5a3820;
    --wood-light: #8a5a34;
    --band: rgba(20, 12, 8, 0.86);
    --band-soft: rgba(20, 12, 8, 0.55);
    --white: #ffffff;
    --green: #7cc242;
    --label: #2b1a12;
    --photo-after-a: #9c8a7c;
    --photo-after-b: #6f8a6a;
    --photo-before-a: #d8d6d0;
    --photo-before-b: #8c8a86;
  }
  * { margin: 0; padding: 0; box-sizing: border-box; }
  html, body {
    width: 1200px; height: 848px; overflow: hidden;
    background: var(--stage);
    font-family: "Lato", sans-serif;
  }
  .flyer {
    position: absolute; left: 310px; top: 14px;
    width: 580px; height: 820px; overflow: hidden;
    box-shadow: 0 10px 40px rgba(0,0,0,0.6);
  }
  .wood-texture {
    position: absolute; inset: 0;
    background:
      linear-gradient(90deg, var(--wood-dark) 0%, var(--wood-mid) 18%, var(--wood-light) 30%, var(--wood-mid) 42%, var(--wood-dark) 55%, var(--wood-mid) 68%, var(--wood-light) 80%, var(--wood-mid) 92%, var(--wood-dark) 100%);
  }
  .top-band {
    position: absolute; left: 0; right: 0; top: 0; height: 78px;
    background: var(--band);
  }
  .title-band {
    position: absolute; left: 0; right: 0; top: 104px; height: 72px;
    background: var(--band-soft);
  }
  .title {
    position: absolute; right: 28px; top: 34px; width: 440px;
    color: var(--white); font-weight: 700; font-size: 34px;
    line-height: 1.15; text-transform: uppercase; text-align: right;
    letter-spacing: 0.5px;
  }
  .photo {
    position: absolute; border: 5px solid var(--white);
  }
  .photo-after {
    left: 34px; top: 196px; width: 410px; height: 250px;
    background: linear-gradient(120deg, var(--photo-after-a), var(--photo-after-b) 55%, var(--photo-after-a));
  }
  .photo-before {
    left: 372px; top: 392px; width: 180px; height: 150px;
    border-width: 4px;
    background: linear-gradient(135deg, var(--photo-before-a), var(--photo-before-b));
  }
  .photo-label {
    position: absolute; background: var(--label); color: var(--white);
    font-weight: 900; font-size: 13px; padding: 5px 10px; letter-spacing: 0.5px;
  }
  .photo-after .photo-label { left: 16px; bottom: 16px; }
  .photo-before .photo-label { right: 10px; bottom: 10px; }
  .info-band {
    position: absolute; left: 0; right: 0; top: 470px; height: 260px;
    background: var(--band);
  }
  .description {
    position: absolute; left: 34px; width: 320px;
    color: var(--white); font-size: 11px; line-height: 1.45;
  }
  .description-top { top: 486px; }
  .description-bottom { top: 660px; width: 500px; }
  .cta {
    position: absolute; left: 34px; top: 566px;
  }
  .cta-line {
    color: var(--white); font-weight: 700; font-size: 20px;
  }
  .phone {
    color: var(--green); font-weight: 900; font-size: 54px; line-height: 1.05;
    letter-spacing: 1px;
  }
</style>
</head>
<body>
  <main class="flyer">
    <div class="wood-texture" role="img" aria-label="Dark wood grain background"></div>
    <div class="top-band"></div>
    <div class="title-band"></div>
    <h1 class="title">Brenwick Doors and Interiors</h1>

    <div class="photo photo-after" role="img" aria-label="After photo of a restored door frame">
      <span class="photo-label">AFTER</span>
    </div>

    <div class="info-band"></div>

    <div class="photo photo-before" role="img" aria-label="Before photo of a worn door with iron hardware">
      <span class="photo-label">BEFORE</span>
    </div>

    <p class="description description-top">Lorem ipsum dolor sit amet, consectetur adipiscing elit. Suspendisse vestibulum feugiat elit, et posuere justo sagittis sit amet. Aliquam lacinia quam vel aliquam efficitur. Ut egestas risus a porta faucibus. Donec mauris mi, laoreet in lacus in, tincidunt pharetra massa.</p>

    <div class="cta">
      <p class="cta-line">Call Us Today For Free Estimate</p>
      <p class="phone">123 456 7890</p>
    </div>

    <p class="description description-bottom">Lorem ipsum dolor sit amet, consectetur adipiscing elit. Suspendisse vestibulum feugiat elit, et posuere justo sagittis sit amet. Aliquam lacinia quam vel aliquam efficitur.</p>
  </main>
</body>
</html>
```